I am looking for a whole Stationery Design for my Company. A new Logo, Letterhead and Business Card. I have attached an old Logo which looks very bad. Be creative and use your own ideas for the Logo as well as all other designs.

```html
<!DOCTYPE html>
<html lang="en">
<head>
<meta charset="utf-8">
<title>Marentle Projects Stationery</title>
<link href="https://fonts.googleapis.com/css2?family=Lato:wght@400;700&display=swap" rel="stylesheet">
<style>
  :root {
    --bg: #d3d4d6;
    --paper: #ffffff;
    --brand: #1d4383;
    --ink: #111111;
    --text: #6b6b6b;
    --watermark: #f6f7f9;
  }
  * { margin: 0; padding: 0; box-sizing: border-box; }
  html, body { width: 1200px; height: 1200px; overflow: hidden; }
  body { background: var(--bg); font-family: "Lato", sans-serif; color: var(--text); position: relative; }
  .sheet { position: absolute; background: var(--paper); overflow: hidden; }
  .band { position: absolute; left: 0; bottom: 0; width: 100%; background: var(--brand); border-top: 3px solid var(--ink); }
  .label { color: var(--brand); }

  .brand { position: absolute; display: flex; flex-direction: column; align-items: center; }
  .brand__dot { border-radius: 50%; background: var(--brand); }
  .brand__name { font-weight: 700; color: var(--ink); white-space: nowrap; }

  /* Letterhead */
  .letterhead { left: 98px; top: 112px; width: 475px; height: 672px; }
  .letterhead .watermark { position: absolute; left: 92px; top: 182px; width: 294px; height: 294px; border-radius: 50%; background: var(--watermark); }
  .letterhead .brand { left: 26px; top: 58px; width: 104px; }
  .letterhead .brand__dot { width: 30px; height: 30px; margin-bottom: 5px; }
  .letterhead .brand__name { font-size: 14px; }
  .letterhead .salutation, .letterhead .date { position: absolute; top: 168px; font-size: 8px; }
  .letterhead .salutation { left: 31px; }
  .letterhead .date { right: 28px; }
  .letterhead .body { position: absolute; left: 31px; right: 28px; top: 200px; font-size: 8.1px; line-height: 12.7px; text-align: justify; }
  .letterhead .body p { margin-bottom: 12px; }
  .letterhead .signature { position: absolute; left: 31px; top: 372px; width: 82px; height: 36px; background: linear-gradient(90deg, #eef0f6, #f7f8fb); }
  .letterhead .signer { position: absolute; left: 31px; top: 414px; }
  .signer__name { font-size: 11.5px; color: #333; }
  .signer__role { font-size: 8px; }
  .letterhead .contacts { position: absolute; left: 0; right: 0; top: 556px; text-align: center; font-size: 8px; line-height: 11.5px; }
  .letterhead .contacts .address { margin-top: 11px; }
  .letterhead .band { height: 40px; }

  /* Business cards */
  .card-front { left: 556px; top: 233px; width: 218px; height: 124px; background: var(--brand); }
  .card-front .brand { left: 0; right: 0; top: 38px; }
  .card-front .brand__dot { width: 26px; height: 26px; background: var(--paper); margin-bottom: 4px; }
  .card-front .brand__name { color: var(--paper); font-size: 12px; }

  .card-back { left: 556px; top: 376px; width: 218px; height: 124px; text-align: center; }
  .card-back .signer { margin-top: 30px; }
  .card-back .signer__name { font-size: 7px; font-weight: 700; color: var(--ink); }
  .card-back .signer__role { font-size: 4.5px; color: #999; }
  .card-back .contacts { margin-top: 12px; font-size: 4.6px; line-height: 7.6px; }
  .card-back .contacts .address { margin-top: 1px; }
  .card-back .band { height: 18px; border-top-width: 2px; }

  /* Envelope back */
  .envelope-back { left: 607px; top: 701px; width: 498px; height: 249px; }
  .envelope-back .flap { position: absolute; left: 0; top: 0; width: 100%; height: 84px; display: block; }
  .envelope-back .flap-dot { position: absolute; left: 223px; top: 17px; width: 52px; height: 52px; border-radius: 50%; background: var(--paper); }

  /* Envelope front */
  .envelope-front { left: 335px; top: 809px; width: 498px; height: 249px; }
  .envelope-front .brand { left: 45px; top: 30px; width: 100px; }
  .envelope-front .brand__dot { width: 30px; height: 30px; margin-bottom: 5px; }
  .envelope-front .brand__name { font-size: 14px; }
  .envelope-front .contacts { position: absolute; left: 45px; top: 112px; font-size: 9.5px; line-height: 12.8px; }
  .envelope-front .contacts .address { margin-top: 11px; }
  .envelope-front .window { position: absolute; left: 287px; top: 104px; width: 173px; height: 79px; border-radius: 14px; border: 2px solid #cfcfcf; background: linear-gradient(100deg, #fafafa 0%, #f0f0f0 45%, #d9d9d9 46%, #f7f7f7 60%, #ffffff 100%); }
  .envelope-front .band { height: 32px; }
</style>
</head>
<body>

<section class="sheet letterhead">
  <div class="watermark"></div>
  <div class="brand"><div class="brand__dot"></div><div class="brand__name">Marentle Projects</div></div>
  <div class="salutation">Dear, Mr___________</div>
  <div class="date">Date : 14.06.2019</div>
  <div class="body">
    <p>Lorem Ipsum is simply dummy text of the printing and typesetting industry. Lorem Ipsum has been the industry's standard dummy text ever since the1500s,when an unknown printer took a galley of type and scrambled it to make a type specimen book. It has survived not only five centuries, but also the leap into electronic typesetting, remaining essentially unchanged.</p>
    <p>Lorem Ipsum is simply dummy text of the printing and typesetting industry. Lorem Ipsum has been the industry's standard dummy text ever since the1500s.</p>
    <p>Lorem Ipsum is simply dummy text of the printing and typesetting industry.</p>
  </div>
  <div class="signature" role="img" aria-label="Handwritten signature"></div>
  <div class="signer"><div class="signer__name">Your Name</div><div class="signer__role">Designation</div></div>
  <div class="contacts">
    <div><span class="label">Phone :</span> 012-555-0147</div>
    <div><span class="label">Email :</span> info@marentleprojects.com</div>
    <div><span class="label">Web :</span> www.marentleprojects.com</div>
    <div class="address"><span class="label">Address :</span> 418 Harbor Ln. Easton, VA 23190</div>
  </div>
  <div class="band"></div>
</section>

<section class="sheet card-front">
  <div class="brand"><div class="brand__dot"></div><div class="brand__name">Marentle Projects</div></div>
</section>

<section class="sheet card-back">
  <div class="signer"><div class="signer__name">Your Name</div><div class="signer__role">Designation</div></div>
  <div class="contacts">
    <div><span class="label">Phone :</span> 012-555-0147</div>
    <div><span class="label">Email :</span> info@marentleprojects.com</div>
    <div><span class="label">Web :</span> www.marentleprojects.com</div>
    <div class="address"><span class="label">Address :</span> 418 Harbor Ln. Easton, VA 23190</div>
  </div>
  <div class="band"></div>
</section>

<section class="sheet envelope-back">
  <svg class="flap" viewBox="0 0 498 84" preserveAspectRatio="none">
    <path d="M0,0 H498 L488,72 Q486,83 474,83 H22 Q10,83 9,72 Z" fill="var(--brand)"/>
  </svg>
  <div class="flap-dot"></div>
</section>

<section class="sheet envelope-front">
  <div class="brand"><div class="brand__dot"></div><div class="brand__name">Marentle Projects</div></div>
  <div class="contacts">
    <div><span class="label">Phone :</span> 012-555-0147</div>
    <div><span class="label">Email :</span> info@marentleprojects.com</div>
    <div><span class="label">Web :</span> www.marentleprojects.com</div>
    <div class="address"><span class="label">Address :</span> 418 Harbor Ln. Easton, VA 23190</div>
  </div>
  <div class="window"></div>
  <div class="band"></div>
</section>

</body>
</html>
```